Create the following for my cosmetic business : Logo and packaging design*

Valiremo Beauty is a cosmetic brand of skincare and makeup. I need:

(1) A logo: That represents creativity, beautiful, powerful and royalty. The logo should be unique and fun at sane time. It should be attractive enough for customers to want to identify with it. target audience is anyone who values beauty. The logo should be designed in a way that it will be visibly printable on different surfaces and sizes of different products

(2). Packaging designs: Unique layout of logo and brand on packages (external packages and designs on the body of the products itself) for skincare products (such as body creams, scrubs, bath soap, facial masks, etc). and make up products such as lipsticks, lip gloss, eyeshadow pallettes, contour, eyelashes etc.

Target Market(s)

Skincare products and cosmetics for:

Age: 16 -45
mid-income earners
Vegan friendly

Industry/Entity Type

Cosmetics

Font styles to use
Sans Serif
Script

Requirements
Must have
• include "animals cruelty-free" symbol in one corner somewhere win the design

very creative designs
Nice to have
• Design variations of
1. Dark Background
2. Light background

so I can compare

```html
<!DOCTYPE html>
<html lang="en">
<head>
<meta charset="utf-8">
<title>Valiremo Beauty – Purifying Skincare Labels</title>
<link rel="stylesheet" href="https://fonts.googleapis.com/css2?family=Jost:wght@300;400;500&family=Oswald:wght@300;400&display=swap">
<style>
  :root {
    --backdrop: #d9d9d9;
    --label-white: #ffffff;
    --rose: #9c5c64;
    --rose-deep: #7e4049;
    --rose-light: #b9828a;
    --rose-text: #a4646c;
    --ink: #2b2b2b;
  }
  * { box-sizing: border-box; margin: 0; padding: 0; }
  html, body { width: 1200px; height: 800px; overflow: hidden; }
  body {
    background: var(--backdrop);
    font-family: "Jost", sans-serif;
  }
  .product-range {
    width: 1200px; height: 800px;
    display: flex; align-items: flex-end; justify-content: center;
    gap: 30px; padding-bottom: 70px;
  }
  .label {
    display: flex; flex-direction: column; align-items: center;
    background: var(--label-white);
    border-radius: 0.8em;
    overflow: hidden;
    box-shadow: 0 10px 30px rgba(0,0,0,0.12);
  }
  .label--scrubs { width: 230px; height: 450px; font-size: 13px; }
  .label--creams { width: 270px; height: 600px; font-size: 16px; }
  .label--soap   { width: 250px; height: 520px; font-size: 14.5px; }
  .label--masks  { width: 200px; height: 400px; font-size: 12px; }

  .brand { display: flex; flex-direction: column; align-items: center; padding-top: 1.6em; }
  .brand-dot {
    width: 2.4em; height: 2.4em; border-radius: 50%;
    border: 2px solid var(--rose-text);
  }
  .brand-name {
    margin-top: 0.6em;
    font-size: 1.35em; font-weight: 400; color: var(--rose-text);
    white-space: nowrap;
  }
  .range-name {
    margin: 1.3em 0 0.9em;
    font-size: 0.72em; font-weight: 500; letter-spacing: 0.75em;
    color: var(--ink); padding-left: 0.75em;
  }
  .feature-band {
    flex: 1; width: 100%;
    display: flex; flex-direction: column; align-items: center; justify-content: center;
    background: linear-gradient(100deg, var(--rose-light) 0%, var(--rose) 45%, var(--rose-deep) 100%);
    color: var(--label-white); text-align: center; padding: 1em 0.6em;
  }
  .product-title {
    font-size: 3em; font-weight: 400; line-height: 0.95; text-transform: uppercase;
  }
  .claim-head {
    margin-top: 0.9em;
    font-family: "Oswald", sans-serif; font-weight: 400; font-size: 0.95em;
  }
  .claim-line {
    font-family: "Oswald", sans-serif; font-weight: 300; font-size: 0.95em; line-height: 1.45;
  }
  .badge-strip {
    width: 100%; display: flex; justify-content: center; gap: 0.9em;
    padding: 0.8em 0;
  }
  .badge {
    width: 3em; height: 3em; border-radius: 50%;
    border: 2px solid var(--rose-text);
  }
  .volume-band {
    width: 100%; height: 2.8em;
    display: flex; align-items: center; justify-content: center;
    background: linear-gradient(100deg, var(--rose) 0%, var(--rose-deep) 100%);
    color: var(--label-white);
    font-family: "Oswald", sans-serif; font-weight: 400; font-size: 1.1em;
  }
</style>
</head>
<body>
<main class="product-range">

  <article class="label label--scrubs">
    <header class="brand"><span class="brand-dot"></span><span class="brand-name">Valiremo Beauty</span></header>
    <p class="range-name">PURIFYING</p>
    <section class="feature-band">
      <h2 class="product-title">Body<br>Scrubs</h2>
      <p class="claim-head">CLEARS BREAKOUTS</p>
      <p class="claim-line">Naturally Derived grapefruit Extract</p>
      <p class="claim-line">Salicylic acid acne treatment</p>
    </section>
    <div class="badge-strip"><span class="badge"></span><span class="badge"></span><span class="badge"></span></div>
    <footer class="volume-band">6.7FL.OZ. /300ML ℮</footer>
  </article>

  <article class="label label--creams">
    <header class="brand"><span class="brand-dot"></span><span class="brand-name">Valiremo Beauty</span></header>
    <p class="range-name">PURIFYING</p>
    <section class="feature-band">
      <h2 class="product-title">Body<br>Creams</h2>
      <p class="claim-head">CLEARS BREAKOUTS</p>
      <p class="claim-line">Naturally Derived grapefruit Extract</p>
      <p class="claim-line">Salicylic acid acne treatment</p>
    </section>
    <div class="badge-strip"><span class="badge"></span><span class="badge"></span><span class="badge"></span></div>
    <footer class="volume-band">6.7FL.OZ. /300ML ℮</footer>
  </article>

  <article class="label label--soap">
    <header class="brand"><span class="brand-dot"></span><span class="brand-name">Valiremo Beauty</span></header>
    <p class="range-name">PURIFYING</p>
    <section class="feature-band">
      <h2 class="product-title">Bath<br>Soap</h2>
      <p class="claim-head">CLEARS BREAKOUTS</p>
      <p class="claim-line">Naturally Derived grapefruit Extract</p>
      <p class="claim-line">Salicylic acid acne treatment</p>
    </section>
    <div class="badge-strip"><span class="badge"></span><span class="badge"></span><span class="badge"></span></div>
    <footer class="volume-band">6.7FL.OZ. /300ML ℮</footer>
  </article>

  <article class="label label--masks">
    <header class="brand"><span class="brand-dot"></span><span class="brand-name">Valiremo Beauty</span></header>
    <p class="range-name">PURIFYING</p>
    <section class="feature-band">
      <h2 class="product-title">Facial<br>Masks</h2>
      <p class="claim-head">CLEARS BREAKOUTS</p>
      <p class="claim-line">Naturally Derived grapefruit Extract</p>
      <p class="claim-line">Salicylic acid acne treatment</p>
    </section>
    <div class="badge-strip"><span class="badge"></span><span class="badge"></span><span class="badge"></span></div>
    <footer class="volume-band">6.7FL.OZ. /100ML ℮</footer>
  </article>

</main>
</body>
</html>
```